Flower delivery business needs sales brochure

I have a courier business that specialises in same-day flower deliveries; I want to make a single page A4 sales brochure (folded to DL) to give to our potential customers.
The company website is petalvanto.com, this will give an idea of who we are and what we do, as well as some graphics and colours that we use.
When opened, the inside A4 space of the brochure will be a pricelist, so the entire page will be an excel table with delivery locations and prices; we will add the prices ourselves later, so ideally the inside will be a background of some sort that won't obstruct text. Maybe light/transparent flowers and a background colour?
The front of the DL brochure should be mostly a title page, so business name, phone number, a graphic?
The first inside page should relate to our service, there's a lot of info on our website that you could use, so same day delivery, 10:30 and 2:30 pick-up times, established over 10 years ago, air-conditioned vans, delivery to 300+ suburbs.
The back page would be contact details and maybe a summary of the key points of the 'about us' section of the website.

Industry/Entity Type

Business

```html
<!DOCTYPE html>
<html lang="en">
<head>
<meta charset="utf-8">
<title>Petal Vanto – Flowers Straight to Your Front Door</title>
<link href="https://fonts.googleapis.com/css2?family=Jura:wght@500&family=Roboto+Condensed:ital,wght@0,300;1,300&display=swap" rel="stylesheet">
<style>
  :root {
    --sunset-orange: #f26a39;
    --warm-amber: #f9a332;
    --sun-yellow: #fdc92c;
    --leaf-green: #76a557;
    --grass-light: #a3bd3f;
    --grass-dark: #55812c;
    --petal-pink: #ec86ab;
    --petal-pink-soft: #f3a9c4;
    --text-light: #ffffff;
  }
  * { margin: 0; padding: 0; box-sizing: border-box; }
  html, body { width: 851px; height: 1200px; overflow: hidden; }
  body { font-family: "Roboto Condensed", Arial, sans-serif; }

  .brochure-page {
    position: relative;
    width: 851px;
    height: 1200px;
    overflow: hidden;
    background: linear-gradient(to bottom, var(--sunset-orange) 0%, var(--warm-amber) 22%, var(--sun-yellow) 42%, var(--sun-yellow) 100%);
  }

  .info-panel {
    position: absolute;
    left: 0; top: 0;
    width: 851px; height: 1200px;
  }

  .meadow-photo {
    position: absolute;
    left: 0; top: 830px;
    width: 851px; height: 370px;
    background: linear-gradient(to bottom, rgba(163,189,63,0) 0%, var(--grass-light) 30%, var(--grass-dark) 100%);
  }

  .headline {
    position: absolute;
    left: 0; top: 111px;
    width: 851px;
    text-align: center;
    font-family: "Jura", "Trebuchet MS", sans-serif;
    font-weight: 500;
    font-size: 44px;
    line-height: 66px;
    letter-spacing: -0.5px;
    color: var(--text-light);
    text-transform: uppercase;
  }
  .headline-line { display: block; }

  .headline-flower-photo {
    position: absolute;
    left: 164px; top: 112px;
    width: 60px; height: 60px;
    border-radius: 50%;
    background: radial-gradient(circle, var(--petal-pink-soft) 0%, var(--petal-pink) 100%);
  }

  .intro-text {
    position: absolute;
    left: 130px; top: 289px;
    width: 590px;
    text-align: center;
    font-weight: 300;
    font-size: 26.5px;
    line-height: 38.4px;
    color: var(--text-light);
  }

  .testimonial {
    position: absolute;
    left: 150px; top: 575px;
    width: 590px;
    text-align: center;
    font-style: italic;
    font-weight: 300;
    font-size: 26.5px;
    line-height: 38.4px;
    color: var(--text-light);
  }

  .quote-mark {
    position: absolute;
    width: 48px; height: 34px;
  }
  .quote-mark--open { left: 102px; top: 562px; }
  .quote-mark--close { left: 689px; top: 672px; }
</style>
</head>
<body>
  <main class="brochure-page">
    <svg class="info-panel" width="851" height="1200" viewBox="0 0 851 1200" aria-hidden="true">
      <polygon points="52,50 798,50 798,834 52,742" fill="var(--leaf-green)"/>
    </svg>

    <div class="headline-flower-photo" role="img" aria-label="Photo of a pink gerbera daisy"></div>
    <h1 class="headline">
      <span class="headline-line">Flowers Straight</span>
      <span class="headline-line">To Your Front Door</span>
    </h1>

    <p class="intro-text">Petal Vanto Pty Ltd is a courier company that<br>specializes in the delivery of flowers and gifts.<br>We offer a same day courier service for the florist<br>&amp; gift retail and wholesale market, and deliver<br>to over 300 suburbs throughout the Brisbane<br>Metropolitan region.</p>

    <svg class="quote-mark quote-mark--open" viewBox="0 0 50 36" aria-hidden="true">
      <path d="M20 2 C8 6 2 14 3 24 C3 31 8 35 13 35 C18 35 21 31 21 27 C21 22 17 19 12 20 C12 13 16 8 22 5 Z" fill="var(--sun-yellow)"/>
      <path d="M47 2 C35 6 29 14 30 24 C30 31 35 35 40 35 C45 35 48 31 48 27 C48 22 44 19 39 20 C39 13 43 8 49 5 Z" fill="var(--sun-yellow)"/>
    </svg>

    <blockquote class="testimonial">We have been in the business for over 10 years,<br>and are very focused on delivering the best<br>customer service possible.</blockquote>

    <svg class="quote-mark quote-mark--close" viewBox="0 0 50 36" aria-hidden="true">
      <path d="M3 34 C15 30 21 22 20 12 C20 5 15 1 10 1 C5 1 2 5 2 9 C2 14 6 17 11 16 C11 23 7 28 1 31 Z" fill="var(--sun-yellow)"/>
      <path d="M30 34 C42 30 48 22 47 12 C47 5 42 1 37 1 C32 1 29 5 29 9 C29 14 33 17 38 16 C38 23 34 28 28 31 Z" fill="var(--sun-yellow)"/>
    </svg>

    <div class="meadow-photo" role="img" aria-label="Photo of a green grass meadow with a pansy, sunflower, gerbera, poppies and a daffodil"></div>
  </main>
</body>
</html>
```